Marcus Delane Consulting Webpage

I need to transition into a Wordpress website to be able to insert tracking code. This was a HostPerch website, but now I'm limited on functionality

Here are requirements: I need to replicate marcusdelane.online

My company is focused in search and placement, consulting and workforce development for the turfgrass and hospitality industry

I'm also looking to integrate the following for a recruiting agency job board.
Multiple Dashboard view
✔ Job map
✔ Demo Content upload
✔ Chat button
✔ CV/Resume builder
✔ Featured job on top
✔ Email Alert
✔ Job bookmark
✔ Job CV package
✔ Social media Login
✔ SEO set up
✔ Plugin installation
✔ Featured jobs
✔ Payment gateway integration and set up
✔ Responsive design
Updates

Went on vacation/holiday

Target Market(s)

Golf and turfgrass businesses; as well as candidates for those companies

Industry/Entity Type

Turfgrass and Golf Industry

Coding

Coded - Design and coding required

Font styles to use
Sans Serif

Colors

Designer to choose colors to be used in the design.

Requirements
Must have
• Functionality of HostPerch Web Design builder, Chat box capability, pop up capability, scheduling/appointment booking integration, ability to upload videos similar to my current website, e-commerce capabilities
Nice to have
• Everything to integrate "recruiting agency" aspect to collect information from potential candidates

```html
<!DOCTYPE html>
<html lang="en">
<head>
<meta charset="utf-8">
<title>Marcus Delane Consulting</title>
<link rel="stylesheet" href="https://fonts.googleapis.com/css2?family=Montserrat:wght@400;500;600;700&display=swap">
<style>
:root{
  --blue:#1a87e0;
  --blue-dark:#1572c2;
  --blue-soft:#5aaef0;
  --ink:#2f3338;
  --muted:#6d7278;
  --line:#e3e6ea;
  --hero-bg:#eff1f4;
  --yellow:#f6c619;
  --white:#fff;
}
*{margin:0;padding:0;box-sizing:border-box}
html,body{width:1200px;height:3729px;overflow:hidden}
body{font-family:'Montserrat',sans-serif;color:var(--ink);background:var(--white);position:relative}
.abs{position:absolute}
a{color:inherit;text-decoration:none}

/* header */
.site-header{position:absolute;left:0;top:0;width:1200px;height:61px;background:var(--white);z-index:5;box-shadow:0 1px 3px rgba(0,0,0,.05)}
.brand-disc{position:absolute;left:148px;top:-20px;width:130px;height:125px;border-radius:0 0 65px 65px;background:var(--white);z-index:6;text-align:center;padding-top:52px}
.brand-name{font-weight:700;font-size:10px;line-height:13px;letter-spacing:.4px;color:var(--ink);white-space:nowrap}
.main-nav{position:absolute;left:363px;top:24px;display:flex;gap:25px;font-size:10px;font-weight:500;color:var(--ink)}
.nav-icons{position:absolute;left:731px;top:21px;display:flex;gap:20px}
.btn-signin{position:absolute;left:850px;top:15px;width:81px;height:31px;border:1px solid #c9cdd2;border-radius:16px;font-size:10px;font-weight:500;text-align:center;line-height:29px}
.btn-join{position:absolute;left:945px;top:15px;width:97px;height:31px;background:var(--blue);color:var(--white);border-radius:16px;font-size:10px;font-weight:600;text-align:center;line-height:31px}

/* hero */
.hero{position:absolute;left:0;top:61px;width:1200px;height:477px;background:linear-gradient(90deg,#f6f7f9,var(--hero-bg));overflow:hidden}
.hero-circle{position:absolute;left:767px;top:-60px;width:434px;height:434px;border-radius:50%;background:var(--blue)}
.hero-ring{position:absolute;left:890px;top:-40px;width:330px;height:330px;border-radius:50%;border:3px solid var(--blue-soft)}
.hero-photo{position:absolute;left:712px;top:10px;width:330px;height:467px;border-radius:150px 150px 0 0;background:linear-gradient(180deg,#d9dde3 0%,#c3c8cf 55%,#9ca3ad 100%)}
.hero-left-circle{position:absolute;left:-55px;top:395px;width:196px;height:196px;border-radius:50%;background:var(--blue);z-index:1}
.hero-kicker{position:absolute;left:158px;top:172px;font-size:29px;font-weight:600;color:var(--ink)}
.hero-title{position:absolute;left:157px;top:206px;font-size:46px;line-height:52px;font-weight:700;color:var(--ink)}
.hero-title span,.accent{color:var(--blue)}
.hero-sub{position:absolute;left:158px;top:327px;font-size:13px;font-weight:700;letter-spacing:3px}
.hero-sub .c{color:var(--blue)}
.search-bar{position:absolute;left:162px;top:381px;width:458px;height:49px;background:var(--white);border:1px solid #d6dade;border-radius:25px;box-shadow:0 3px 8px rgba(0,0,0,.06);font-size:10px;color:var(--muted);padding:16px 0 0 40px}
.search-btn{position:absolute;left:627px;top:382px;width:47px;height:47px;border-radius:50%;background:var(--blue)}

/* featured */
.section-title{position:absolute;width:1200px;text-align:center;font-size:26px;font-weight:600;color:var(--ink)}
.job-card{position:absolute;width:198px;height:250px;background:var(--white);box-shadow:0 2px 10px rgba(0,0,0,.12)}
.job-img{width:198px;height:104px}
.job-card h3{font-size:12px;font-weight:500;margin:12px 0 0 10px}
.job-card p{font-size:8px;color:var(--muted);margin:6px 10px 0 10px;line-height:12px}
.job-meta{display:flex;justify-content:space-between;font-size:8px;color:var(--muted);margin:12px 12px 0 10px}
.job-foot{display:flex;justify-content:space-between;align-items:center;margin:15px 10px 0 10px;font-size:8px;color:var(--muted)}
.btn-apply{background:var(--blue);color:var(--white);font-size:9px;font-weight:700;padding:7px 13px;border-radius:13px}
.chevron{position:absolute;left:586px;top:949px;width:29px;height:29px;border-radius:50%;background:var(--white);border:1px solid #cfd3d8;z-index:3}

/* categories */
.categories{position:absolute;left:0;top:965px;width:1200px;height:374px;background:linear-gradient(180deg,#1c7fd2,#1d8ae2);overflow:hidden}
.cat-circle{position:absolute;width:166px;height:166px;border-radius:50%;border:2px solid rgba(255,255,255,.8);padding:6px}
.cat-circle div{width:100%;height:100%;border-radius:50%}
.cat-label{position:absolute;width:300px;text-align:center;color:var(--white);font-size:14px;font-weight:600}
.cat-divider{position:absolute;left:599px;top:120px;height:190px;border-left:1px dashed rgba(255,255,255,.55)}
.white-bubble{position:absolute;border-radius:50%;background:var(--white);z-index:2}

/* services */
.service{position:absolute;width:210px}
.service h3{font-size:17px;font-weight:500;margin-top:12px;white-space:nowrap}
.service p{font-size:10px;color:var(--muted);line-height:14px;margin-top:8px;width:180px}
.dot-btn{display:block;width:22px;height:22px;border-radius:50%;background:var(--blue);margin-top:14px}
.service-link{position:absolute;top:1502px;height:1px;width:90px;background:#9fcbf1}

/* about */
.about-photo{position:absolute;left:159px;top:1669px;width:335px;height:379px;background:linear-gradient(180deg,#8a9a83 0%,#c7b9a4 45%,#3a3f47 100%)}
.about-title{position:absolute;left:537px;top:1664px;font-size:26px;font-weight:600}
.about-lead{position:absolute;left:539px;top:1720px;width:485px;font-size:13px;line-height:18px}
.about-small{position:absolute;left:540px;top:1791px;width:440px;font-size:9px;line-height:14px;color:var(--muted)}
.btn-read{position:absolute;left:537px;top:1851px;width:97px;height:28px;border-radius:14px;background:var(--blue);color:var(--white);font-size:10px;font-weight:600;text-align:center;line-height:28px}
.awards{position:absolute;left:384px;top:1925px;width:655px;height:219px;background:var(--blue);border-radius:14px;color:var(--white);padding:30px 20px 0 32px}
.awards li{list-style:none;font-size:15px;line-height:22px;padding-left:28px;position:relative;margin-bottom:9px}
.awards li::before{content:"";position:absolute;left:0;top:5px;border-left:10px solid var(--white);border-top:6px solid transparent;border-bottom:6px solid transparent}
.awards li::after{content:"";position:absolute;left:2px;top:8px;border-left:5px solid var(--blue);border-top:3px solid transparent;border-bottom:3px solid transparent}

/* compare */
.rule{position:absolute;height:1px;background:var(--line)}
.side-img{position:absolute;width:186px;height:317px;top:2320px}
.compare-card{position:absolute;left:347px;top:2323px;width:445px;height:319px;background:var(--white);box-shadow:0 2px 12px rgba(0,0,0,.12)}
.compare-img{position:absolute;left:392px;top:2281px;width:148px;height:116px;background:linear-gradient(180deg,#a9c9e6,#3a5570 70%,#7f9cb5);z-index:2}
.compare-title{position:absolute;left:562px;top:2358px;font-size:21px;font-weight:500}
.rating{position:absolute;left:392px;top:2409px;font-size:9px;color:var(--muted);display:flex;gap:6px;align-items:center}
.rating .stars{color:var(--blue);font-size:14px;letter-spacing:1px}
.compare-text{position:absolute;left:392px;top:2441px;width:360px;font-size:11px;line-height:18px;color:var(--muted)}
.stats{position:absolute;left:393px;top:2513px;display:flex}
.stat{width:84px;font-size:11px}
.stat b{display:block;font-size:21px;color:var(--blue);font-weight:500;margin-top:4px}
.btn-solid,.btn-ghost{position:absolute;top:2587px;height:29px;border-radius:15px;font-size:9px;font-weight:600;text-align:center;line-height:27px}
.btn-solid{left:393px;width:104px;background:var(--blue);color:var(--white);border:1px solid var(--blue)}
.btn-ghost{left:505px;width:85px;border:1px solid #b9bec4;color:var(--ink);font-weight:500}

/* news */
.news{position:absolute;left:0;top:2720px;width:1200px;height:579px;background:var(--blue);overflow:hidden}
.news-title{position:absolute;width:1200px;top:50px;text-align:center;color:var(--white);font-size:26px;font-weight:600}
.news-title::after{content:"";display:block;width:24px;height:2px;background:var(--white);margin:8px auto 0}
.news-card{position:absolute;width:271px;height:367px;border:1px solid rgba(255,255,255,.7);background:rgba(255,255,255,.04);color:var(--white)}
.news-img{width:269px;height:155px}
.news-card h3{font-size:19px;font-weight:400;line-height:24px;margin:19px 20px 0 21px}
.news-card .date{font-size:9px;font-weight:600;margin:12px 0 0 21px}
.news-card p{font-size:9px;line-height:13px;margin:8px 20px 0 21px;opacity:.9}
.news-card .arrow{position:absolute;left:21px;bottom:22px;width:24px;height:24px;border-radius:50%;background:var(--white)}

/* cta */
.cta-title{position:absolute;left:156px;top:3328px;font-size:26px;font-weight:600}
.cta-sub{position:absolute;left:157px;top:3370px;font-size:14px;color:#555}
.btn-start{position:absolute;left:912px;top:3341px;width:130px;height:28px;border-radius:14px;background:var(--yellow);font-size:10px;font-weight:600;text-align:center;line-height:28px}

/* footer */
.footer-brand{position:absolute;left:125px;top:3520px;font-weight:700;font-size:15px;line-height:19px;text-align:center;width:200px;white-space:nowrap}
.footer-contact{position:absolute;left:157px;font-size:12px;display:flex;gap:10px;align-items:center;white-space:nowrap}
.footer-col{position:absolute;top:3456px}
.footer-col h4{font-size:13px;font-weight:600;margin-bottom:14px}
.footer-col li{list-style:none;font-size:13px;color:#444;margin-bottom:12px}
.newsletter-input{position:absolute;left:870px;top:3490px;width:172px;height:33px;border:1px solid #cfd3d8;background:#f6f7f8;font-size:9px;color:var(--muted);padding:11px 0 0 26px}
.btn-sub{position:absolute;left:868px;top:3538px;width:91px;height:28px;border-radius:14px;background:var(--blue);color:var(--white);font-size:10px;font-weight:600;text-align:center;line-height:28px}
.social{position:absolute;top:3586px;width:28px;height:28px;border-radius:50%}
.copyright{position:absolute;top:3690px;width:1200px;text-align:center;font-size:12px;color:#555}
</style>
</head>
<body>

<header class="site-header">
  <nav class="main-nav"><a>HOME</a><a>JOBS</a><a>EMPLOYERS</a><a>CANDIDATES</a><a>PACKAGES</a></nav>
  <div class="nav-icons">
    <svg width="17" height="17" viewBox="0 0 17 17" fill="none" stroke="#555" stroke-width="1.2"><circle cx="8.5" cy="8.5" r="7"/><path d="M8.5 5v7M5 8.5h7"/></svg>
    <svg width="17" height="17" viewBox="0 0 17 17" fill="none" stroke="#555" stroke-width="1.2"><path d="M4 12V8a4.5 4.5 0 019 0v4l1.5 1.5h-12zM7 15h3"/></svg>
    <svg width="17" height="17" viewBox="0 0 17 17" fill="none" stroke="#555" stroke-width="1.4"><circle cx="7" cy="7" r="5"/><path d="M11 11l4.5 4.5"/></svg>
  </div>
  <a class="btn-signin">SIGN IN</a>
  <a class="btn-join">JOIN&nbsp; NOW</a>
</header>
<div class="brand-disc"><div class="brand-name">MARCUS DELANE<br>CONSULTING</div></div>

<section class="hero">
  <div class="hero-circle"></div>
  <div class="hero-ring"></div>
  <div class="hero-photo" role="img" aria-label="Smiling young professional holding a laptop and waving"></div>
</section>
<div class="hero-left-circle"></div>
<div class="hero-kicker">WE CREATE</div>
<h1 class="hero-title">SUSTAINABLE <span>TALENT</span><br>SOLUTIONS</h1>
<div class="hero-sub">FOR THE <span class="c">TURFGRASS</span>, <span class="c">GREEN</span> AND <span class="c">CLUB INDUSTRIES</span></div>
<div class="search-bar">Job Title, Keyword, Company, Location
  <svg class="abs" style="left:22px;top:20px" width="9" height="9" viewBox="0 0 9 9" fill="none" stroke="#888"><circle cx="4" cy="4" r="3"/><path d="M6 6l2.5 2.5"/></svg>
  <svg class="abs" style="left:420px;top:20px" width="12" height="8" viewBox="0 0 12 8" fill="none" stroke="#666" stroke-width="1.4"><path d="M1 1l5 5 5-5"/></svg>
</div>
<div class="search-btn"><svg width="47" height="47" viewBox="0 0 47 47" fill="none" stroke="#fff" stroke-width="2"><circle cx="22" cy="22" r="6"/><path d="M26.5 26.5l5 5"/></svg></div>

<h2 class="section-title" style="top:589px">FEATURED <span class="accent">JOB</span></h2>

<article class="job-card" style="left:158px;top:647px">
  <div class="job-img" role="img" aria-label="Hands typing on a laptop with charts" style="background:linear-gradient(135deg,#cfd8d2,#7fb38f 60%,#e9e4da)"></div>
  <h3>Property Manager</h3>
  <p>Sed ut perspiciatis unde omnis iste natus error sit voluptatem</p>
  <div class="job-meta"><span>&#9673; London E16 1XL</span><span>&#9638; Nov, 2022</span></div>
  <div class="job-foot"><span>5 Years of Exp.</span><span class="btn-apply">APPLY NOW</span></div>
</article>
<article class="job-card" style="left:386px;top:647px">
  <div class="job-img" role="img" aria-label="Waitress in a restaurant dining room" style="background:linear-gradient(135deg,#e9e1d3,#c9a98a 55%,#f4efe6)"></div>
  <h3>Waiter/Waitres</h3>
  <p>Sed ut perspiciatis unde omnis iste natus error sit voluptatem</p>
  <div class="job-meta"><span>&#9673; London E16 1XL</span><span>&#9638; Nov, 2022</span></div>
  <div class="job-foot"><span>5 Years of Exp.</span><span class="btn-apply">APPLY NOW</span></div>
</article>
<article class="job-card" style="left:616px;top:650px">
  <div class="job-img" role="img" aria-label="Business people in an office meeting" style="background:linear-gradient(135deg,#243a5e,#5a6f8f 55%,#d6cfc6)"></div>
  <h3>Logistics Porter</h3>
  <p>Sed ut perspiciatis unde omnis iste natus error sit voluptatem</p>
  <div class="job-meta"><span>&#9673; London E16 1XL</span><span>&#9638; Nov, 2022</span></div>
  <div class="job-foot"><span>5 Years of Exp.</span><span class="btn-apply">APPLY NOW</span></div>
</article>
<article class="job-card" style="left:845px;top:653px">
  <div class="job-img" role="img" aria-label="Presenter beside a whiteboard sketch about management" style="background:linear-gradient(135deg,#e8ecf2,#b7c3d3 55%,#f3f5f8)"></div>
  <h3>Team Leader</h3>
  <p>Sed ut perspiciatis unde omnis iste natus error sit voluptatem</p>
  <div class="job-meta"><span>&#9673; London E16 1XL</span><span>&#9638; Nov, 2022</span></div>
  <div class="job-foot"><span>5 Years of Exp.</span><span class="btn-apply">APPLY NOW</span></div>
</article>

<div class="chevron"><svg width="27" height="27" viewBox="0 0 27 27" fill="none" stroke="#777" stroke-width="1.3"><path d="M9 12l4.5 4.5L18 12"/></svg></div>

<section class="categories" role="img" aria-label="Blue tinted aerial view of a city park">
  <h2 class="section-title" style="top:48px;color:#fff">BROWSE JOBS BY CATEGORIES</h2>
  <div class="cat-circle" style="left:360px;top:111px"><div role="img" aria-label="Golf course with trees and flowers" style="background:linear-gradient(180deg,#bfe0f5 0%,#5c8f3c 55%,#3d6b2a 100%)"></div></div>
  <div class="cat-circle" style="left:671px;top:111px"><div role="img" aria-label="Resort hotel with a swimming pool" style="background:linear-gradient(180deg,#cfe3f4 0%,#e8eef4 45%,#5ea0d8 100%)"></div></div>
  <div class="cat-divider"></div>
  <div class="cat-label" style="left:291px;top:297px">Turfgrass industry</div>
  <div class="cat-label" style="left:614px;top:297px">Hospitality industry</div>
</section>
<div class="white-bubble" style="left:1085px;top:1213px;width:232px;height:232px"></div>

<div class="service" style="left:171px;top:1390px">
  <svg width="74" height="72" viewBox="0 0 74 72" fill="none" stroke="#1a87e0" stroke-width="2"><rect x="2" y="2" width="68" height="58" rx="2"/><path d="M2 12h68"/><circle cx="8" cy="7" r="1.3"/><circle cx="13" cy="7" r="1.3"/><circle cx="35" cy="38" r="14"/><path d="M28 33h14M28 38h14M28 43h10M25 48l-14 14"/></svg>
  <h3>Search and placement</h3>
  <p>Sed ut perspiciatis unde omnis iste natus error sit voluptatem accusa ntium doloremque laudantium</p>
  <span class="dot-btn"><svg width="22" height="22" viewBox="0 0 22 22" fill="none" stroke="#fff" stroke-width="1.6"><path d="M9.5 7l4 4-4 4"/></svg></span>
</div>
<div class="service-link" style="left:389px"></div>
<div class="service" style="left:504px;top:1390px">
  <svg width="76" height="72" viewBox="0 0 76 72" fill="none" stroke="#1a87e0" stroke-width="2"><circle cx="14" cy="10" r="7"/><circle cx="46" cy="12" r="8"/><circle cx="66" cy="28" r="7"/><circle cx="30" cy="36" r="9"/><circle cx="12" cy="56" r="8"/><circle cx="52" cy="56" r="9"/><path d="M19 15l5 14M38 16l-4 12M39 38l20-6M23 42l-6 8M37 43l8 7"/></svg>
  <h3>Consulting</h3>
  <p>Sed ut perspiciatis unde omnis iste natus error sit voluptatem accusa ntium doloremque laudantium</p>
  <span class="dot-btn"><svg width="22" height="22" viewBox="0 0 22 22" fill="none" stroke="#fff" stroke-width="1.6"><path d="M9.5 7l4 4-4 4"/></svg></span>
</div>
<div class="service-link" style="left:717px"></div>
<div class="service" style="left:841px;top:1390px">
  <svg width="76" height="72" viewBox="0 0 76 72" fill="none" stroke="#1a87e0" stroke-width="2"><rect x="16" y="2" width="42" height="24" rx="12"/><path d="M26 12h22M26 18h16M22 26l-4 6 10-6"/><circle cx="18" cy="44" r="7"/><path d="M4 70c0-10 6-16 14-16s14 6 14 16z"/><circle cx="54" cy="44" r="7"/><path d="M40 70c0-10 6-16 14-16s14 6 14 16z"/></svg>
  <h3>Workforce development</h3>
  <p>Sed ut perspiciatis unde omnis iste natus error sit voluptatem accusa ntium doloremque laudantium</p>
  <span class="dot-btn"><svg width="22" height="22" viewBox="0 0 22 22" fill="none" stroke="#fff" stroke-width="1.6"><path d="M9.5 7l4 4-4 4"/></svg></span>
</div>

<div class="about-photo" role="img" aria-label="Portrait of Marcus in a suit on a golf course"></div>
<h2 class="about-title">ABOUT <span class="accent">MARCUS</span></h2>
<p class="about-lead">Marcus's passion for the game of golf began at the age of 6.&nbsp; After playing high school golf, Marcus attended Keystone State University to study Turfgrass Science.</p>
<p class="about-small">He interned at three top 50 golf courses - Ashbrook Golf Club, Red Mesa Country Club for the 2007 National Pro Championship, and Cedar Hollow Golf Club for the 2008 Founders Tournament</p>
<a class="btn-read">READ MORE</a>
<ul class="awards">
  <li>2020 Turf Managers Guild Hale Award</li>
  <li>2019 "Best Blog" presented by Greenwell Labs and Fairway Trade magazine</li>
  <li>2020 Peter Lund Award recognized for Leadership in Social Media presented by Greenwell Labs and Fairway Trade magazine</li>
</ul>

<div class="rule" style="left:0;top:2236px;width:380px"></div>
<div class="rule" style="left:820px;top:2236px;width:380px"></div>
<h2 class="section-title" style="top:2219px">COMPARE <span class="accent">REVIEWS &amp; SALARIES</span></h2>
<div class="side-img" style="left:114px;background:linear-gradient(180deg,#6faee6,#3f8fd6)" role="img" aria-label="Blue tinted photo of a hospitality worker on the phone"></div>
<div class="side-img" style="left:837px;background:linear-gradient(180deg,#4d8fcf,#2f73b8)" role="img" aria-label="Blue tinted aerial view of a city park"></div>
<div class="compare-card"></div>
<div class="compare-img" role="img" aria-label="Glass office tower against the sky"></div>
<h3 class="compare-title">Hospitality Assistant</h3>
<div class="rating"><span class="stars">★★★★★</span><span style="color:var(--blue)">(5.0 rating)</span><span>Northgate Polymers - Riverton, OH</span></div>
<p class="compare-text">Sed ut perspiciatis unde omnis iste natus error sit volu ptatem accusa ntium doloremque laudantium</p>
<div class="rule" style="left:393px;top:2498px;width:364px;background:#d5d9de"></div>
<div class="stats">
  <div class="stat">Jobs<b>102</b></div>
  <div class="stat">Reviews<b>1254</b></div>
  <div class="stat" style="width:106px">Salaries<b>4569</b></div>
  <div class="stat">Interviews<b>510</b></div>
</div>
<div class="rule" style="left:393px;top:2571px;width:364px;background:#d5d9de"></div>
<a class="btn-solid">SEARCH JOB</a>
<a class="btn-ghost">FOLLOW</a>

<section class="news">
  <h2 class="news-title">LATEST NEWS</h2>
  <article class="news-card" style="left:158px;top:126px">
    <div class="news-img" role="img" aria-label="Golf course with trees under a cloudy sky" style="background:linear-gradient(180deg,#c5d6e6 0%,#7d9a6a 55%,#4f7a3a 100%)"></div>
    <h3>Who is Registered Apprenticeship for?</h3>
    <div class="date">December 9, 2021</div>
    <p>The goal of Registered Apprenticeship is to identify individuals who could potentially be a long-term fit in their field, but need either experience or education to take the next steps.</p>
    <span class="arrow"><svg width="24" height="24" viewBox="0 0 24 24" fill="none" stroke="#1a87e0" stroke-width="1.6"><path d="M10.5 8l4 4-4 4"/></svg></span>
  </article>
  <article class="news-card" style="left:453px;top:126px">
    <div class="news-img" role="img" aria-label="Island green surrounded by water" style="background:linear-gradient(180deg,#dfe8f0 0%,#6f9a4c 45%,#4c7fa6 100%)"></div>
    <h3>Fairway Trade - Firm &amp; Fast</h3>
    <div class="date">October 27, 2021</div>
    <p>First off, the labor market is tiresome … and periodically frustrating. Sourcing, interviewing, hiring and training challenges are not absent from our service to clients. If anything,</p>
    <span class="arrow"><svg width="24" height="24" viewBox="0 0 24 24" fill="none" stroke="#1a87e0" stroke-width="1.6"><path d="M10.5 8l4 4-4 4"/></svg></span>
  </article>
  <article class="news-card" style="left:748px;top:134px">
    <div class="news-img" role="img" aria-label="Golfer silhouetted against a sunset" style="background:linear-gradient(180deg,#6a5a5a 0%,#d88a4a 55%,#2b2a2e 100%)"></div>
    <h3>Looking for a Few Good Assistants</h3>
    <div class="date">December 4, 2021</div>
    <p>Dale Harmon discuss solutions and challenges golf courses face in attracting qualified, educated and industry trained employees.</p>
    <span class="arrow"><svg width="24" height="24" viewBox="0 0 24 24" fill="none" stroke="#1a87e0" stroke-width="1.6"><path d="M10.5 8l4 4-4 4"/></svg></span>
  </article>
</section>
<div class="white-bubble" style="left:-113px;top:3158px;width:226px;height:226px"></div>

<h2 class="cta-title">LOOKING FOR A <span class="accent">JOB?</span></h2>
<p class="cta-sub">Brows hundreds of job offers &amp; find the best suitable posion.</p>
<a class="btn-start">GET STARTED NOW</a>
<div class="rule" style="left:0;top:3416px;width:1200px"></div>

<footer>
  <div class="footer-brand">MARCUS DELANE<br>CONSULTING</div>
  <div class="footer-contact" style="top:3577px"><svg width="12" height="12" viewBox="0 0 12 12" fill="none" stroke="#444"><path d="M2 1h3l1 3-1.5 1a7 7 0 003 3L9 6.5l3 1v3a1 1 0 01-1 1C5.5 11.5.5 6.5.5 2a1 1 0 011-1z"/></svg>555.014.2387</div>
  <div class="footer-contact" style="top:3602px"><svg width="13" height="10" viewBox="0 0 13 10" fill="none" stroke="#444"><rect x=".5" y=".5" width="12" height="9"/><path d="M.5.5l6 5 6-5"/></svg>info@marcusdelane.online</div>
  <div class="footer-col" style="left:376px"><h4>FOR JOB SEEEKERS</h4><ul><li>Create account</li><li>Post CV</li><li>Job seeker FAQ</li><li>Video Guides</li><li>Advanced job search</li></ul></div>
  <div class="footer-col" style="left:627px"><h4>FOR EMPLOYEES</h4><ul><li>Post job</li><li>CV Search</li><li>Search Resume</li><li>Sitemap</li><li>Help</li></ul></div>
  <div class="footer-col" style="left:870px"><h4>NEWSLETTER SIGN UP</h4></div>
  <div class="newsletter-input">Enter Your Email
    <svg class="abs" style="left:9px;top:13px" width="10" height="8" viewBox="0 0 10 8" fill="none" stroke="#888"><rect x=".5" y=".5" width="9" height="7"/><path d="M.5.5l4.5 4 4.5-4"/></svg>
  </div>
  <a class="btn-sub">SUBCRIBE</a>
  <span class="social" style="left:872px;background:#3a5aa8" role="img" aria-label="Social profile link"></span>
  <span class="social" style="left:909px;border:1px solid #b9bec4" role="img" aria-label="Social profile link"></span>
  <span class="social" style="left:949px;border:1px solid #b9bec4" role="img" aria-label="Social profile link"></span>
  <div class="rule" style="left:0;top:3665px;width:1200px"></div>
  <p class="copyright">Copyright © 2022 MDelane, LLC - All Rights Reserved.</p>
</footer>

</body>
</html>
```